Established Australian Supplement Brand ready to introduce new flavours

We're an established Australian Nutraceuticals/Supplement brand with a signature Whey Protein product and are about to introduce 3 new protein flavours - Vanilla Maple, Strawberry and Caramel. These are the flavours that we need new packaging for. The image below is just to show our current product for inspiration.
We currently have one existing flavour and packaging and would like to expand upon this, maintaining brand congruency with colours, style and feel.
Our core focusses as a brand are on high quality, minimal ingredients with a clean and energetic feel. Our mantra is "Making it easier for you to be healthier" and have a mission to bring better health across the world.
Whilst our brand is of a premium and high quality nature, we want to begin injecting more personality and brand into the packaging.
We have existing pre-print designs from our current product so the foundations are already set.
We're just looking to make some minor adjustments to the current packaging to suit the new flavours.
Attached below is our current product to provide the scope of how the packaging currently looks.
Health and Wellness

```html
<!DOCTYPE html>
<html lang="en">
<head>
<meta charset="UTF-8">
<title>Clear Core Blend – Flavour Range Packaging</title>
<link href="https://fonts.googleapis.com/css2?family=Montserrat:wght@700;800&family=Nunito+Sans:wght@400&family=Barlow+Semi+Condensed:wght@500&family=Quicksand:wght@600&display=swap" rel="stylesheet">
<style>
  :root {
    --backdrop: #e3e3e3;
    --pouch: #fbfbfb;
    --ink: #2b2b2b;
    --leaf: #a8d2d3;
    --leaf-deep: #7fb9bb;
    --strawberry: #ea8f9c;
    --strawberry-tag: #e8304f;
    --maple: #e67650;
    --maple-tag: #de4b46;
    --caramel: #e3a247;
    --caramel-tag: #e9832f;
  }
  * { box-sizing: border-box; margin: 0; padding: 0; }
  html, body { width: 1200px; height: 900px; overflow: hidden; }
  body { background: var(--backdrop); position: relative; font-family: "Nunito Sans", sans-serif; }

  .pouch {
    position: absolute;
    width: 340px;
    height: 470px;
    background: var(--pouch);
    border-radius: 6px;
    overflow: hidden;
    box-shadow: 0 10px 24px rgba(0,0,0,0.08);
    display: flex;
    flex-direction: column;
    align-items: center;
    padding-top: 92px;
    --accent: var(--ink);
    --tag: var(--ink);
  }
  .pouch--strawberry { left: 55px;  top: 300px; --accent: var(--strawberry); --tag: var(--strawberry-tag); }
  .pouch--maple      { left: 430px; top: 90px;  --accent: var(--maple);      --tag: var(--maple-tag); }
  .pouch--caramel    { left: 805px; top: 210px; --accent: var(--caramel);    --tag: var(--caramel-tag); }

  .leaf-art { position: absolute; background: radial-gradient(ellipse at 40% 45%, var(--leaf) 0%, var(--leaf-deep) 70%, transparent 72%); opacity: 0.75; }
  .leaf-art--top    { width: 150px; height: 110px; top: -18px; right: -10px; transform: rotate(-18deg); }
  .leaf-art--side   { width: 60px;  height: 130px; top: 110px; right: -18px; transform: rotate(12deg); opacity: 0.6; }
  .leaf-art--bottom { width: 130px; height: 80px;  bottom: -26px; left: -6px; opacity: 0.55; }

  .product-name {
    font-family: "Montserrat", sans-serif;
    font-weight: 800;
    color: var(--accent);
    font-size: 40px;
    line-height: 1.2;
    letter-spacing: 3px;
    text-align: center;
    position: relative;
  }
  .tagline {
    margin-top: 18px;
    font-family: "Montserrat", sans-serif;
    font-weight: 700;
    font-size: 9px;
    letter-spacing: 5px;
    color: var(--accent);
    position: relative;
  }
  .descriptor {
    margin-top: 26px;
    font-size: 8.5px;
    line-height: 1.35;
    text-align: center;
    color: var(--ink);
    position: relative;
  }
  .flavour-art {
    margin-top: 16px;
    width: 34px;
    height: 34px;
    border-radius: 50%;
    background: var(--tag);
    opacity: 0.85;
  }
  .flavour-tag {
    margin-top: 10px;
    background: var(--tag);
    color: #fff;
    font-family: "Quicksand", sans-serif;
    font-weight: 600;
    font-size: 11px;
    padding: 1px 5px 2px;
  }
  .net-weight {
    margin-top: 20px;
    font-family: "Barlow Semi Condensed", sans-serif;
    font-weight: 500;
    font-size: 10.5px;
    letter-spacing: 0.8px;
    color: var(--ink);
  }
  .brand {
    margin-top: 24px;
    display: flex;
    flex-direction: column;
    align-items: center;
    gap: 6px;
    font-family: "Nunito Sans", sans-serif;
    font-size: 10px;
    letter-spacing: 3px;
    color: var(--ink);
  }
  .brand__dot { width: 12px; height: 12px; border-radius: 50%; border: 1px solid var(--ink); }
</style>
</head>
<body>

  <section class="pouch pouch--strawberry">
    <div class="leaf-art leaf-art--top" role="img" aria-label="Sketched teal ivy leaf illustration"></div>
    <div class="leaf-art leaf-art--side" role="img" aria-label="Sketched teal ivy leaf illustration"></div>
    <div class="leaf-art leaf-art--bottom" role="img" aria-label="Sketched teal ivy leaf illustration"></div>
    <h1 class="product-name">CLEAR CORE<br>BLEND</h1>
    <p class="tagline">FUEL THE GOOD DAYS</p>
    <p class="descriptor">Whey Protein Isolate<br>Formulated supplementary sports food</p>
    <div class="flavour-art" role="img" aria-label="Strawberry illustration"></div>
    <p class="flavour-tag">Strawberry</p>
    <p class="net-weight">NET 1KG | 30 SERVES*</p>
    <div class="brand"><span class="brand__dot"></span><span>FERNWELL</span></div>
  </section>

  <section class="pouch pouch--maple">
    <div class="leaf-art leaf-art--top" role="img" aria-label="Sketched teal ivy leaf illustration"></div>
    <div class="leaf-art leaf-art--side" role="img" aria-label="Sketched teal ivy leaf illustration"></div>
    <div class="leaf-art leaf-art--bottom" role="img" aria-label="Sketched teal ivy leaf illustration"></div>
    <h1 class="product-name">CLEAR CORE<br>BLEND</h1>
    <p class="tagline">FUEL THE GOOD DAYS</p>
    <p class="descriptor">Whey Protein Isolate<br>Formulated supplementary sports food</p>
    <div class="flavour-art" role="img" aria-label="Maple leaf illustration"></div>
    <p class="flavour-tag">Vanilla Maple</p>
    <p class="net-weight">NET 1KG | 30 SERVES*</p>
    <div class="brand"><span class="brand__dot"></span><span>FERNWELL</span></div>
  </section>

  <section class="pouch pouch--caramel">
    <div class="leaf-art leaf-art--top" role="img" aria-label="Sketched teal ivy leaf illustration"></div>
    <div class="leaf-art leaf-art--side" role="img" aria-label="Sketched teal ivy leaf illustration"></div>
    <div class="leaf-art leaf-art--bottom" role="img" aria-label="Sketched teal ivy leaf illustration"></div>
    <h1 class="product-name">CLEAR CORE<br>BLEND</h1>
    <p class="tagline">FUEL THE GOOD DAYS</p>
    <p class="descriptor">Whey Protein Isolate<br>Formulated supplementary sports food</p>
    <div class="flavour-art" role="img" aria-label="Caramel cubes illustration"></div>
    <p class="flavour-tag">Caramel</p>
    <p class="net-weight">NET 1KG | 30 SERVES*</p>
    <div class="brand"><span class="brand__dot"></span><span>FERNWELL</span></div>
  </section>

</body>
</html>
```